【タイトル】
超現実派エンジニアも驚く!
メンタル不調も!恋愛の失敗も!実らない努力も!

全ての原因は56種の「モヤリンk」
最強ワークで過去を手放し、人生を全て好転させよう! 

【書籍の特典情報】
誰でもできる
「セルフ解放ワーク」
の動画プレゼント!

【ターゲット】
引き寄せの法則や成功法則が好きな方向け

【著者】
(元システムエンジニア)
企業サポーター
桐野 沙織

【説明】
電子書籍の表紙のデザインをお願いします。

電子書籍なので、タイトル文字を見やすくしてほしいです。

元システムエンジニアで、企業サポーターという職業柄もあり
とても現実派の私が実感して提供しているワークのお話になります

引き寄せやスピリチュアルとは違うので、
どちらかというと成功の法則のように
現実的なイメージの表紙だと良いかなと思っています。

本文をつけますので参考にしていただければと思います。

見た時に、とてもインパクトがあるように感じました。
電子書籍は、表紙の役割が大きいので
わかりやすさもとても大切だと感じ、選ばせていただきました。

皆様、素敵なデザインをご提案いただきありがとうございます。
とても迷い、投票も行い選択させていただきました。
今後、お仕事やデザインをご依頼させていただく際は
また、よろしくお願いいたします。

```html
<!DOCTYPE html>
<html lang="ja">
<head>
<meta charset="UTF-8">
<title>最強ワークで過去を手放し、人生を全て好転させよう!</title>
<link rel="stylesheet" href="https://fonts.googleapis.com/css2?family=Noto+Sans+JP:wght@400;500;700&display=swap">
<style>
  :root {
    --pink: #e0457a;
    --ink: #1a1a1a;
    --paper: #ffffff;
    --sky-top: #c9b6c4;
    --sky-mid: #ead6d6;
    --glow: #fbe9df;
    --cube: #f4f1ef;
  }
  html, body { margin: 0; padding: 0; overflow: hidden; }
  body { width: 750px; height: 1200px; background: var(--paper); }
  .cover {
    position: relative;
    width: 750px;
    height: 1200px;
    background: var(--paper);
    font-family: "Noto Sans JP", sans-serif;
    color: var(--ink);
    overflow: hidden;
  }
  .hero-photo {
    position: absolute;
    left: 0; top: 0;
    width: 750px; height: 632px;
    background:
      radial-gradient(ellipse 420px 300px at 600px 470px, var(--glow) 0%, rgba(251,233,223,0) 70%),
      linear-gradient(90deg, var(--cube) 0%, rgba(244,241,239,0.85) 28%, rgba(244,241,239,0) 55%),
      linear-gradient(180deg, var(--sky-top) 0%, var(--sky-mid) 55%, #f1dcd6 100%);
  }
  .main-title {
    position: absolute;
    left: 338px; top: 58px;
    margin: 0;
    font-weight: 500;
    font-size: 47px;
    line-height: 75px;
    letter-spacing: 1px;
    color: var(--ink);
  }
  .tagline {
    position: absolute;
    left: 0; width: 750px;
    text-align: center;
    margin: 0;
  }
  .tagline--lead { top: 650px; font-size: 44px; font-weight: 700; color: var(--pink); }
  .tagline--symptoms { top: 726px; font-size: 25px; font-weight: 500; color: var(--ink); }
  .tagline--cause { top: 775px; font-size: 56px; font-weight: 500; color: var(--pink); }
  .tagline--keyword { top: 852px; font-size: 100px; font-weight: 500; color: var(--pink); line-height: 1.2; }
  .author {
    position: absolute;
    left: 40px; top: 1068px;
  }
  .author__career, .author__role { margin: 0; font-size: 17px; line-height: 26px; }
  .author__name { margin: 6px 0 0; font-size: 36px; font-weight: 500; }
  .author__romaji { font-size: 15px; letter-spacing: 2px; margin-left: 12px; }
  .bonus {
    position: absolute;
    right: 52px; top: 1068px;
    text-align: center;
  }
  .bonus__label { margin: 0; font-size: 16px; font-weight: 700; color: var(--pink); }
  .bonus__line { margin: 4px 0 0; font-size: 20px; font-weight: 500; color: var(--pink); }
</style>
</head>
<body>
<div class="cover">
  <div class="hero-photo" role="img" aria-label="白い立方体の上に座り、淡いピンクの夕空を眺める女性の後ろ姿"></div>

  <h1 class="main-title">最強ワークで<br>過去を手放し、<br>人生を全て<br>好転させよう!</h1>

  <p class="tagline tagline--lead">超現実派エンジニアも驚く!</p>
  <p class="tagline tagline--symptoms">メンタル不調も!&nbsp;恋愛の失敗も!&nbsp;実らない努力も!</p>
  <p class="tagline tagline--cause">全ての原因は56種の</p>
  <p class="tagline tagline--keyword">モヤリンk</p>

  <div class="author">
    <p class="author__career">[元システムエンジニア]</p>
    <p class="author__role">企業サポーター</p>
    <p class="author__name">桐野 沙織<span class="author__romaji">KIRINO SAORI</span></p>
  </div>

  <div class="bonus">
    <p class="bonus__label">読者限定プレゼント</p>
    <p class="bonus__line">誰でもできる</p>
    <p class="bonus__line">「セルフ解放ワーク」</p>
  </div>
</div>
</body>
</html>
```